Bottle label design for a mulberry brandy

Please create a label design for a mulberry brandy. The registered brand name is "Kolvat"
The brandy will be produced in Armenia from 100% mulberry.
Color of the product: transparent.
The product will be sold worldwide. The price will be between 30 and 50 USD. So the product will be in premium category.
Therefore we need a solid design, appropriate to the product price category. The design, however, needs to be modern and optimistic.
You can have mulberries on the label or not have, it is up to you.
We have chosen for the product some bottle types, the links to the available bottles you can find in the attachment. Ideally you show a picture of your label on the bottle you selected.

Target Market(s)

worldwide

```html
<!DOCTYPE html>
<html lang="en">
<head>
<meta charset="utf-8">
<title>Kolvat Mulberry Brandy – Label</title>
<link rel="stylesheet" href="https://fonts.googleapis.com/css2?family=Federo&family=Old+Standard+TT:wght@400;700&display=swap">
<style>
  :root {
    --page: #f5f5f3;
    --gold-light: #f4d9a6;
    --gold: #ecbd69;
    --gold-deep: #e2a94a;
    --band: #ffffff;
    --ink: #2b2320;
    --rule: #3a2f2a;
  }
  html, body {
    margin: 0;
    padding: 0;
    width: 1200px;
    height: 1000px;
    overflow: hidden;
    background: var(--page);
  }
  .label {
    position: relative;
    width: 1200px;
    height: 1000px;
  }
  .label svg { position: absolute; inset: 0; }
  .brand-name {
    font-family: "Federo", sans-serif;
    font-size: 150px;
    fill: var(--ink);
    letter-spacing: 2px;
  }
  .volume, .strength {
    font-family: "Old Standard TT", serif;
    font-size: 18px;
    fill: var(--ink);
  }
  .product-name {
    font-family: "Old Standard TT", serif;
    font-weight: 700;
    font-size: 40px;
    fill: var(--ink);
    letter-spacing: 1px;
  }
  .origin {
    font-family: "Old Standard TT", serif;
    font-size: 14px;
    fill: var(--ink);
  }
</style>
</head>
<body>
  <main class="label">
    <svg width="1200" height="1000" viewBox="0 0 1200 1000" xmlns="http://www.w3.org/2000/svg">
      <defs>
        <linearGradient id="gold-field" x1="0" y1="0" x2="1" y2="1">
          <stop offset="0" stop-color="var(--gold-light)"/>
          <stop offset="0.55" stop-color="var(--gold)"/>
          <stop offset="1" stop-color="var(--gold-deep)"/>
        </linearGradient>
      </defs>

      <!-- gold diagonal field -->
      <polygon class="gold-field" points="290,395 916,80 1030,395 1000,600 950,600 276,920 245,600 240,560" fill="url(#gold-field)"/>

      <!-- emblem area above the band -->
      <rect class="emblem" x="610" y="200" width="320" height="186" rx="10" fill="#cfa35a" opacity="0.55" role="img" aria-label="Emblem: a striding lion holding a sprig of mulberries"/>

      <!-- white name band -->
      <path class="name-band" d="M205,395 L1045,395 Q1065,497 1045,600 L205,600 Q185,497 205,395 Z" fill="var(--band)"/>
      <rect class="band-rule" x="262" y="388" width="780" height="5" fill="var(--rule)"/>
      <rect class="band-rule" x="262" y="594" width="780" height="5" fill="var(--rule)"/>

      <text class="volume" x="222" y="505">700ml</text>
      <text class="brand-name" x="610" y="548" text-anchor="middle">Kolvat</text>
      <text class="strength" x="1000" y="505">38%vol</text>

      <text class="product-name" x="334" y="665">MULBERRY</text>
      <text class="product-name" x="334" y="710">BRANDY</text>
      <text class="origin" x="334" y="752">DISTILLED AND BOTTLED</text>
      <text class="origin" x="334" y="770">IN ARMENIA</text>
    </svg>
  </main>
</body>
</html>
```